Doctor's Office Intake Forms

Hi,

I am looking to have the following form to be replicated and combined with the other files. I do not want this form merely digitized but a new form to be created but asking the same questions with our logo etc. Please add a section for allergies and medications taken. For the Sexually transmitted infections the choices are the ones listed plus Pelvic Inflammatory Disease, Syphilis, HIV, and Hepatitis.

Please use common sense. The example file provided is a print out of a digital intake form.

Medical

Sans Serif

• Good format

```html
<!DOCTYPE html>
<html lang="en">
<head>
<meta charset="utf-8">
<title>Kindred Care – Patient Onboarding Forms</title>
<link href="https://fonts.googleapis.com/css2?family=Montserrat:ital,wght@0,400;0,500;0,600;0,700;0,800;1,500&display=swap" rel="stylesheet">
<style>
:root{
  --backdrop:#4b4c50;
  --blue:#2f6cf2;
  --purple:#8b3fe0;
  --pink:#f0407f;
  --orange:#ff6a2b;
  --panel:#ddebfb;
  --line:#c6cfdc;
  --ink:#222631;
  --muted:#3b3f4a;
  --brand-grad:linear-gradient(90deg,#2f6cf2 0%,#8b3fe0 40%,#f0407f 72%,#ff6a2b 100%);
  --blue-grad:linear-gradient(90deg,#2f6cf2,#7a45e6);
  --pink-grad:linear-gradient(90deg,#f0407f,#c23fd9);
}
*{box-sizing:border-box;margin:0;padding:0}
html,body{width:1200px;height:4000px;overflow:hidden}
body{background:var(--backdrop);position:relative;font-family:'Montserrat',sans-serif;color:var(--ink)}

.page{position:absolute;width:505px;background:#fff;overflow:hidden}
.col-left{left:78px}.col-right{left:612px}
.row-1{top:127px;height:652px}
.row-2{top:850px;height:652px}
.row-3{top:1573px;height:662px}
.row-4{top:2304px;height:662px}
.row-5{top:3045px;height:664px}

/* header */
.brand{position:absolute;left:24px;top:30px;display:flex;align-items:center;gap:10px}
.brand-dot{width:40px;height:40px;border-radius:50%;background:var(--blue)}
.brand-name{font-weight:800;font-size:25px;color:var(--blue);letter-spacing:.5px}
.form-tab{position:absolute;right:0;top:24px;width:182px;text-align:center}
.form-tab .tab{background:var(--brand-grad);color:#fff;font-weight:700;font-size:10.5px;height:18px;line-height:18px;border-radius:10px 0 0 10px;letter-spacing:.3px}
.form-tab .tab-note{font-style:italic;font-weight:500;font-size:8.5px;color:var(--orange);margin-top:3px}

/* footer */
.footer{position:absolute;left:0;right:0;bottom:0;height:30px}
.footer-bar{height:4px;background:linear-gradient(90deg,var(--blue) 0 36%,var(--purple) 36% 68%,var(--orange) 68% 100%)}
.footer-items{display:flex;justify-content:space-between;padding:8px 34px 0 26px;font-size:8.5px;font-weight:500}
.footer-items span{display:flex;align-items:center;gap:7px}
.footer-items i{width:12px;height:12px;border-radius:50%;display:inline-block}
.dot-blue{background:var(--blue)}.dot-purple{background:var(--purple)}.dot-orange{background:var(--orange)}

/* body */
.content{position:absolute;top:100px;left:0;right:0}
.panel{background:var(--panel);padding:10px 26px 14px}
.plain{padding:10px 26px}
.pill{display:block;width:max-content;margin:0 auto 12px;padding:0 34px;height:18px;line-height:18px;border-radius:10px;color:#fff;font-weight:700;font-size:10px;letter-spacing:.3px}
.pill-blue{background:var(--blue-grad)}
.pill-pink{background:var(--pink-grad)}
.banner{margin:20px 26px 18px;height:20px;line-height:20px;border-radius:10px;background:var(--brand-grad);color:#fff;text-align:center;font-weight:700;font-size:10.5px;letter-spacing:.3px}

.grid{display:grid;gap:0 8px;margin-bottom:8px}
.g1{grid-template-columns:1fr}.g2{grid-template-columns:1fr 1fr}.g3{grid-template-columns:1fr 1fr 1fr}
.field label{display:block;font-size:7px;font-weight:700;text-transform:uppercase;margin-bottom:3px;color:var(--ink)}
.field label em{font-style:normal;color:var(--orange)}
.box{height:15px;background:#fff;border:1px solid var(--line)}
.box.tall{height:34px}
.box.mid{height:24px}

.check{display:inline-flex;align-items:center;gap:4px;font-size:7px;font-weight:700;margin-right:10px}
.check b{width:13px;height:13px;border:1px solid var(--line);background:#fff;display:inline-block}

/* copy pages */
.copy{padding:0 26px;font-size:8.3px;line-height:1.38;color:var(--muted)}
.copy p{margin-bottom:9px}
.copy .lead{color:var(--blue);font-weight:700}
.copy strong{color:var(--ink);font-weight:700}
.copy ul{list-style:none;margin-bottom:9px}
.copy ul li::before{content:"• ";color:var(--pink)}
.copy ol{padding-left:12px;margin-bottom:9px}
.copy ol li{margin-bottom:7px;padding-left:4px}
.copy.justified p{text-align:justify}
.copy h2{font-size:9.5px;color:var(--blue);font-weight:700;margin:4px 0 10px}
.privacy-line{font-size:9.5px;font-weight:600;color:var(--ink);display:flex;align-items:center;gap:6px;margin-bottom:10px}
.email-pill{background:var(--blue);color:#fff;border-radius:10px;padding:2px 10px;font-weight:700;font-size:9px}
.thanks{color:var(--pink);font-weight:600;font-size:9px}
.sign-line{margin:18px 26px 0;border-top:1px solid #9aa2ae}

/* history table */
.visit{display:grid;grid-template-columns:1.3fr 1.3fr .7fr;gap:8px;margin-bottom:12px}
.visit .field label{text-transform:none;font-size:6.8px}
.history{display:grid;grid-template-columns:1fr 1fr 1fr;gap:10px}
.hcol{display:grid;grid-template-columns:1fr 16px 16px;gap:5px 3px;align-items:center;font-size:6.8px;font-weight:700;text-transform:uppercase;align-content:start}
.hcol .hd{font-size:6.8px;text-align:center}
.hcol .sti{color:var(--orange);font-size:6.5px;line-height:1.1}
.hcol .mixed{text-transform:none}
.hcol b{width:14px;height:14px;border:1px solid var(--line);background:#fff;display:block}

/* lifestyle */
.qs{padding:0 26px}
.qs .q{font-size:7px;font-weight:700;text-transform:uppercase;margin-bottom:3px}
.qs .a{margin-bottom:6px}
.qs .count{width:16px;height:13px;border:1px solid var(--line);margin-bottom:6px}
.use-grid{display:grid;grid-template-columns:1fr 1fr;gap:4px 14px;margin-bottom:6px}
.use-grid div{display:flex;align-items:center;font-size:7px;font-weight:700}
.use-grid div span{width:58px}
.drug-grid{display:grid;grid-template-columns:1fr 1fr;gap:4px 14px;margin-bottom:6px;width:320px}
.drug-grid div{display:flex;align-items:center;font-size:7px;font-weight:700}
.drug-grid div span{width:56px}

.sign-grid{display:grid;grid-template-columns:1fr 1fr;gap:14px 14px;padding:6px 26px}
.sign-grid .field label{text-align:center;margin-bottom:8px}
.sign-grid .box{height:60px}
</style>
</head>
<body>

<!-- Page 1: name, background, contact -->
<section class="page col-left row-1">
  <div class="brand"><span class="brand-dot"></span><span class="brand-name">KINDRED CARE</span></div>
  <div class="form-tab"><div class="tab">ONBOARDING FORM</div><div class="tab-note">(Please Read and Sign)</div></div>
  <div class="content">
    <div class="panel">
      <span class="pill pill-blue">NAME AND GENDER</span>
      <div class="grid g1"><div class="field"><label>First Name</label><div class="box"></div></div></div>
      <div class="grid g1"><div class="field"><label>Middle Name</label><div class="box"></div></div></div>
      <div class="grid g1"><div class="field"><label>Last Name</label><div class="box"></div></div></div>
      <div class="grid g3"><div class="field"><label>Suffix</label><div class="box"></div></div><div class="field"><label>Nickname</label><div class="box"></div></div><div class="field"><label>Sex</label><div class="box"></div></div></div>
      <div class="grid g3"><div class="field"><label>Gender Identity</label><div class="box"></div></div><div class="field"><label>Sexual Orientation</label><div class="box"></div></div></div>
      <span class="pill pill-blue" style="margin-top:12px">PATIENT BACKGROUND</span>
      <div class="grid g2"><div class="field"><label>Date of Birth</label><div class="box"></div></div><div class="field"><label>Social Security</label><div class="box"></div></div></div>
      <div class="grid g3" style="margin-bottom:0"><div class="field"><label>Preferred Language</label><div class="box"></div></div><div class="field"><label>Race</label><div class="box"></div></div><div class="field"><label>Ethnicity</label><div class="box"></div></div></div>
    </div>
    <div class="panel" style="margin-top:8px">
      <span class="pill pill-blue">CONTACT INFORMATION</span>
      <div class="grid g3"><div class="field"><label>Email Address</label><div class="box"></div></div><div class="field"><label>Cell Phone</label><div class="box"></div></div><div class="field"><label>Work Phone</label><div class="box"></div></div></div>
      <div class="grid g1"><div class="field"><label>Address</label><div class="box"></div></div></div>
      <div class="grid g3"><div class="field"><label>City</label><div class="box"></div></div><div class="field"><label>State</label><div class="box"></div></div><div class="field"><label>Zip Code</label><div class="box"></div></div></div>
      <div class="grid g3" style="margin-bottom:0"><div class="field"><label><em>Emergency Contact</em> Name</label><div class="box"></div></div><div class="field"><label>Relation</label><div class="box"></div></div><div class="field"><label>Phone</label><div class="box"></div></div></div>
    </div>
  </div>
  <footer class="footer"><div class="footer-bar"></div><div class="footer-items"><span><i class="dot-blue"></i>+1 (555) 010 2480</span><span><i class="dot-purple"></i>info@kindredcare.org</span><span><i class="dot-orange"></i>www.kindredcare.org</span></div></footer>
</section>

<!-- Page 2: patient assistance fund -->
<section class="page col-right row-1">
  <div class="brand"><span class="brand-dot"></span><span class="brand-name">KINDRED CARE</span></div>
  <div class="content">
    <div class="banner">KINDRED CARE PATIENT ASSISTANCE FUND</div>
    <div class="copy">
      <p class="lead">Kindred Care Alliance Inc is a FREE clinic for all that need it.</p>
      <p>Any patient making less than 250K for a single-member household or under 500k for a multi-member household is eligible to enroll in our patient assistance fund.</p>
      <p class="lead">The patient assistance fund covers:</p>
      <ul>
        <li>Any patient responsibility for medical services including</li>
        <li>Co-Payments</li>
        <li>Co-Insurance</li>
        <li>Deductibles</li>
        <li>Out of Pocket Cost</li>
        <li>No Insurance Coverage</li>
      </ul>
      <p>The patient assistance fund DOES NOT cover costs of medications, HOWEVER, Kindred Care works with various patient assistance programs to bring the cost of medications down to little to no cost for our patients.</p>
      <p><strong>If accepted into the patient assistance fund, your insurance may still be billed but Kindred Care Alliance Inc will not bill you.</strong></p>
      <p>By signing this document you attest that you meet the income requirements for the Kindred Care Patient Assistance fund. If you choose not to apply, you may be billed for any out of pocket expenses that you may be responsible for.</p>
    </div>
  </div>
  <footer class="footer"><div class="footer-bar"></div><div class="footer-items"><span><i class="dot-blue"></i>+1 (555) 010 2480</span><span><i class="dot-purple"></i>info@kindredcare.org</span><span><i class="dot-orange"></i>www.kindredcare.org</span></div></footer>
</section>

<!-- Page 3: additional info, medication, allergies, conditions -->
<section class="page col-left row-2">
  <div class="brand"><span class="brand-dot"></span><span class="brand-name">KINDRED CARE</span></div>
  <div class="form-tab"><div class="tab">ONBOARDING FORM</div><div class="tab-note">(Please Read and Sign)</div></div>
  <div class="content">
    <div class="panel">
      <span class="pill pill-blue">ADDITIONAL INFORMATION</span>
      <div class="grid g2"><div class="field"><label>Preferred Pronouns</label><div class="box"></div></div><div class="field"><label>Who Referred You</label><div class="box"></div></div></div>
      <div class="grid g2" style="margin-bottom:4px"><div class="field"><label>Do You Use Online Scheduling</label><span class="check"><b></b>YES</span><span class="check"><b></b>NO</span></div><div class="field"><label>Want Access to Online Portal</label><span class="check"><b></b>YES</span><span class="check"><b></b>NO</span></div></div>
      <div class="grid g1" style="margin-bottom:0"><div class="field"><label>Anything Special We Need to Know</label><div class="box tall"></div></div></div>
    </div>
    <div class="plain">
      <span class="pill pill-pink" style="margin-top:6px">CHANGES TO MEDICATION</span>
      <div class="grid" style="grid-template-columns:2fr 1fr"><div class="field"><label>Medication</label><div class="box"></div></div><div class="field"><label>Dosage</label><div class="box"></div></div></div>
      <div class="grid g1"><div class="field"><label>Indication</label><div class="box"></div></div></div>
      <span class="pill pill-pink" style="margin-top:12px">CHANGES TO ALLERGIES</span>
      <div class="grid g2"><div class="field"><label>Allergy</label><div class="box"></div></div><div class="field"><label>Reaction</label><div class="box"></div></div></div>
      <div class="grid g1"><div class="field"><label>Changes to Allergies</label><div class="box"></div></div></div>
      <span class="pill pill-pink" style="margin-top:12px">CHANGES TO MEDICAL CONDITIONS</span>
      <div class="grid g1"><div class="field"><label>Problem</label><div class="box"></div></div></div>
      <div class="grid g2"><div class="field"><label>Code</label><div class="box"></div></div><div class="field"><label>Status</label><div class="box"></div></div></div>
      <div class="grid g1"><div class="field"><label>Diagnosed</label><div class="box tall"></div></div></div>
    </div>
  </div>
  <footer class="footer"><div class="footer-bar"></div><div class="footer-items"><span><i class="dot-blue"></i>+1 (555) 010 2480</span><span><i class="dot-purple"></i>info@kindredcare.org</span><span><i class="dot-orange"></i>www.kindredcare.org</span></div></footer>
</section>

<!-- Page 4: assignment of benefits -->
<section class="page col-right row-2">
  <div class="brand"><span class="brand-dot"></span><span class="brand-name">KINDRED CARE</span></div>
  <div class="content">
    <div class="banner">ASSIGNMENT OF BENEFITS AND AUTHORIZATION</div>
    <div class="copy">
      <p>While Kindred Care Alliance Inc is waiting for payment for all of the fees, I agree to provide the office with information and forms regarding any source of potential payment, to assist in any way I can, and:</p>
      <ol>
        <li>I hereby assign Kindred Care Alliance Inc my rights to receive payments from the insurance companies responsible for my claim.</li>
        <li>I also hereby authorize the direct payment to Kindred Care Alliance Inc of any sum I now or hereafter owe by any insurance company obligated to make payment to me or you based in whole or in part upon the charges made for your services.</li>
        <li>You are authorized to release any information including the diagnosis and records of any such treatment to any insurance company to process any claims for reimbursement of charges incurred.</li>
      </ol>
      <p><strong>THIS IS A DIRECT ASSIGNMENT OF MY RIGHTS AND BENEFITS UNDER THIS POLICY.</strong></p>
      <p>If you have applied for the Kindred Care Patient Assistance fund, you will not be billed for any balances or out of pocket costs.</p>
    </div>
  </div>
  <footer class="footer"><div class="footer-bar"></div><div class="footer-items"><span><i class="dot-blue"></i>+1 (555) 010 2480</span><span><i class="dot-purple"></i>info@kindredcare.org</span><span><i class="dot-orange"></i>www.kindredcare.org</span></div></footer>
</section>

<!-- Page 5: insurance, visit reasons, medical history -->
<section class="page col-left row-3">
  <div class="brand"><span class="brand-dot"></span><span class="brand-name">KINDRED CARE</span></div>
  <div class="form-tab"><div class="tab">ONBOARDING FORM</div><div class="tab-note">(Please Read and Sign)</div></div>
  <div class="content">
    <div class="panel">
      <span class="pill pill-blue">PRIMARY INSURANCE</span>
      <div class="grid g2"><div class="field"><label>Insurance Company</label><div class="box"></div></div><div class="field"><label>Plan Name</label><div class="box"></div></div></div>
      <div class="grid g2"><div class="field"><label>Insurance ID Number</label><div class="box"></div></div><div class="field"><label>Group Number</label><div class="box"></div></div></div>
      <div class="grid g2" style="margin-bottom:0"><div class="field"><label>Patient Student Status</label><div class="box"></div></div><div class="field"><label>Are You the Insurance Subscriber</label><div class="box"></div></div></div>
    </div>
    <div class="plain">
      <span class="pill pill-pink" style="margin-top:6px">REASONS FOR VISIT</span>
      <div class="visit">
        <div class="field"><label>HEPATITIS C<br>(Prevention, Testing, and Treatment)</label><span class="check"><b></b>YES</span><span class="check"><b></b>NO</span></div>
        <div class="field"><label>HIV<br>(Prevention, Testing, and Treatment)</label><span class="check"><b></b>YES</span><span class="check"><b></b>NO</span></div>
        <div class="field"><label>Are You On PrEP?<br>&nbsp;</label><span class="check"><b></b>YES</span><span class="check"><b></b>NO</span></div>
      </div>
      <span class="pill pill-pink">PERSONAL MEDICAL HISTORY</span>
      <div class="history">
        <div class="hcol">
          <span></span><span class="hd">YES</span><span class="hd">NO</span>
          <span>Anxiety</span><b></b><b></b>
          <span>Asthma</span><b></b><b></b>
          <span>Depression</span><b></b><b></b>
          <span>Diabetes</span><b></b><b></b>
          <span>Heart Disease</span><b></b><b></b>
          <span>High Blood Pressure</span><b></b><b></b>
          <span>Hepatitis/Liver Dysfunction</span><b></b><b></b>
        </div>
        <div class="hcol">
          <span></span><span class="hd">YES</span><span class="hd">NO</span>
          <span>Cancer</span><b></b><b></b>
          <span>High Cholesterol</span><b></b><b></b>
          <span>HIV/AIDS</span><b></b><b></b>
          <span>Kidney Disease</span><b></b><b></b>
          <span>Mental Health Condition</span><b></b><b></b>
          <span>Neurological Condition</span><b></b><b></b>
        </div>
        <div class="hcol">
          <span class="sti">Sexually Transmitted Infection</span><span class="hd">YES</span><span class="hd">NO</span>
          <span class="mixed">Pelvic Inflammatory Disease</span><b></b><b></b>
          <span class="mixed">Syphilis</span><b></b><b></b>
          <span class="mixed">Chlamydia</span><b></b><b></b>
          <span class="mixed">Gonorrhea</span><b></b><b></b>
          <span class="mixed">Herpe</span><b></b><b></b>
          <span class="mixed">HPV</span><b></b><b></b>
          <span class="mixed">HIV</span><b></b><b></b>
          <span class="mixed">Hepatitis</span><b></b><b></b>
        </div>
      </div>
      <div class="field" style="width:310px;margin-top:-18px"><label>Allergies<br>What Are You Allergic To:</label><div class="box"></div></div>
    </div>
  </div>
  <footer class="footer"><div class="footer-bar"></div><div class="footer-items"><span><i class="dot-blue"></i>+1 (555) 010 2480</span><span><i class="dot-purple"></i>info@kindredcare.org</span><span><i class="dot-orange"></i>www.kindredcare.org</span></div></footer>
</section>

<!-- Page 6: informed consent -->
<section class="page col-right row-3">
  <div class="brand"><span class="brand-dot"></span><span class="brand-name">KINDRED CARE</span></div>
  <div class="form-tab"><div class="tab">INFORMED CONSENT</div><div class="tab-note">(Please Read and Sign)</div></div>
  <div class="content">
    <div class="copy justified" style="font-size:8px">
      <p><strong>I hereby request and consent to the performance of medical services on me (or on the patient named below, for whom I am legally responsible) by the staff or consultants employed or contracted at the Kindred Care Alliance Inc. This includes medical services including but not limited to examination, testing, and treatment of various diseases including HIV, sexually transmitted infections, or any diseases conditions that I present for.</strong></p>
      <p>I understand that the results of the tests may have to be reported to the proper government agencies and by signing this agreement I agree to have my information released to any government organization.</p>
      <p>I understand and I am informed that, as is with all healthcare procedures and treatments there are some risks including, but not limited to punctures, abrasions, cuts, infections, misdiagnoses and injuries possibly resulting in death. I do not expect the provider to be able to anticipate and explain all risks and complications, and I wish to rely on the provider to exercise judgment during the course of the procedure with which the provider feels at the time, based upon the facts then known, is in my best interests.</p>
      <p>I also understand that any information not provided to my provider cannot be taken into consideration for my healthcare needs. I understand that with any test, there is a chance for false positives and negatives as well as injury. I will hold harmless the Regional Health Authority and the Kindred Care Alliance Inc, its employees, contractors, and subsidiaries for any damages or injuries that I may suffer as a result of being a patient at the Kindred Care Alliance Inc. These risks also include psychological or physical harm which can result in permanent disability, emotional loss, death or damage to personal property.</p>
      <p>I understand and have been informed that I have the right to a second opinion and secure other opinions if I have concerns as to the nature of my symptoms and treatment options. I have had the chance to inform the office of any or all previous medical conditions or medications that I may have been diagnosed with or prescribed and that information is accurate to the best of my ability.</p>
      <p>I enter into this agreement freely and understand that its duration will last for as long as I am a patient of the Kindred Care Alliance Inc.</p>
      <p>I have read, or have had read to me, the above consent. I am 18 years or older or a representative of a minor/person that has been deemed by the courts to be under my care.</p>
      <p style="margin-bottom:0">This document is governed by the laws of our state.<br>If you are a minor or if you are being represented by another party please provide the appropriate person's:</p>
    </div>
    <div class="sign-line" style="margin-top:22px"></div>
  </div>
  <footer class="footer"><div class="footer-bar"></div><div class="footer-items"><span><i class="dot-blue"></i>+1 (555) 010 2480</span><span><i class="dot-purple"></i>info@kindredcare.org</span><span><i class="dot-orange"></i>www.kindredcare.org</span></div></footer>
</section>

<!-- Page 7: lifestyle questions -->
<section class="page col-left row-4">
  <div class="brand"><span class="brand-dot"></span><span class="brand-name">KINDRED CARE</span></div>
  <div class="form-tab"><div class="tab">ONBOARDING FORM</div><div class="tab-note">(Please Read and Sign)</div></div>
  <div class="content">
    <span class="pill pill-blue" style="margin-top:6px">ADDITIONAL INFORMATION</span>
    <div class="qs">
      <p class="q">Do You Use</p>
      <div class="use-grid">
        <div><span>ALCOHOL</span><span class="check"><b></b>YES</span><span class="check"><b></b>NO</span></div>
        <div><span>ILLICIT DRUGS</span><span class="check"><b></b>YES</span><span class="check"><b></b>NO</span></div>
        <div><span>CIGARETTES</span><span class="check"><b></b>YES</span><span class="check"><b></b>NO</span></div>
        <div><span>SMOKE</span><span class="check"><b></b>YES</span><span class="check"><b></b>NO</span></div>
      </div>
      <p class="q">How Many Sexual Partners Have You Had in the Last 30 Days?</p><div class="count"></div>
      <p class="q">How Many Sexual Partners Have You Had in Your Lifetime?</p><div class="count"></div>
      <p class="q">Do You Use Condoms?</p><div class="a"><span class="check"><b></b>YES</span><span class="check"><b></b>NO</span></div>
      <p class="q">Do You Engage in Anal Sex?</p><div class="a"><span class="check"><b></b>YES</span><span class="check"><b></b>NO</span></div>
      <p class="q">Do You Engage in Oral Sex?</p><div class="a"><span class="check"><b></b>YES</span><span class="check"><b></b>NO</span></div>
      <p class="q">Do You Engage in Vaginal Sex?</p><div class="a"><span class="check"><b></b>YES</span><span class="check"><b></b>NO</span></div>
      <p class="q">Do You Consider Yourself a Sex Worker?</p><div class="a"><span class="check"><b></b>YES</span><span class="check"><b></b>NO</span></div>
      <p class="q">Is There a Chance You May Be Pregnant?</p><div class="a"><span class="check"><b></b>YES</span><span class="check"><b></b>NO</span></div>
      <p class="q">Do You or Someone You Have Sex With Inject Drugs?</p><div class="a"><span class="check"><b></b>YES</span><span class="check"><b></b>NO</span></div>
      <p class="q">Do You Use Street Drugs<br>(We Do Not Judge. This Is for Us to Be Able to Provide You With the Best Possible Healthcare)</p>
      <div class="drug-grid">
        <div><span>COCAINE</span><span class="check"><b></b>YES</span><span class="check"><b></b>NO</span></div><div></div>
        <div><span>METH</span><span class="check"><b></b>YES</span><span class="check"><b></b>NO</span></div>
        <div><span>PILLS</span><span class="check"><b></b>YES</span><span class="check"><b></b>NO</span></div>
        <div><span>HEROIN</span><span class="check"><b></b>YES</span><span class="check"><b></b>NO</span></div>
        <div><span>MDMA</span><span class="check"><b></b>YES</span><span class="check"><b></b>NO</span></div>
      </div>
      <p class="q">Do You Have Sex With Anonymous Partners?</p><div class="a"><span class="check"><b></b>YES</span><span class="check"><b></b>NO</span></div>
    </div>
  </div>
  <footer class="footer"><div class="footer-bar"></div><div class="footer-items"><span><i class="dot-blue"></i>+1 (555) 010 2480</span><span><i class="dot-purple"></i>info@kindredcare.org</span><span><i class="dot-orange"></i>www.kindredcare.org</span></div></footer>
</section>

<!-- Page 8: PHI consent -->
<section class="page col-right row-4">
  <div class="brand"><span class="brand-dot"></span><span class="brand-name">KINDRED CARE</span></div>
  <div class="form-tab"><div class="tab">INFORMED CONSENT</div><div class="tab-note">(Please Read and Sign)</div></div>
  <div class="content">
    <div class="copy justified">
      <h2>CONSENT AUTHORIZATION TO USE OR DISCLOSE PROTECTED HEALTH INFORMATION</h2>
      <p>Your authorization is requested for purposes of delivering your care in an open-door environment as described in the office's privacy notice.</p>
      <p>In the course of your care, in this environment, routine details of your condition and care may be disclosed to other patients or staff in the approximate vicinity of where your care is being delivered. We cannot assure that any of the details of your care will be addressed and considered as confidential by other patients.</p>
      <p>We are requesting your authorization in this regard to assure that you are fully informed and in agreement with the method and circumstances in which we deliver treatment. Your care will not be conditioned on your agreement to this authorization. You have the right not to sign this authorization and you also have the right to revoke this authorization at a later date if that is your wish. If you wish to revoke this authorization at some time in the future please advise us accordingly in writing. You always have the right to review our most updated PHI information.</p>
      <div class="privacy-line">You can also contact our privacy officer at <span class="email-pill">info@kindredcare.org</span></div>
      <p>By signing this agreement, you also agree to allow Kindred Care Alliance Inc to release any and all of your information to entities it has working relationships with including pharmacies, nursing services, and third-party payers.</p>
      <p>If you agree to this authorization and have received and reviewed our office's HIPAA privacy notice please sign and date below. A copy of this authorization will be maintained by this office.</p>
      <p class="thanks">Thank you for your cooperation and understanding.</p>
      <p style="margin-bottom:0">If you are a minor or if you are being represented by another party please provide the appropriate person's:</p>
    </div>
    <div class="sign-line" style="margin-top:22px"></div>
  </div>
  <footer class="footer"><div class="footer-bar"></div><div class="footer-items"><span><i class="dot-blue"></i>+1 (555) 010 2480</span><span><i class="dot-purple"></i>info@kindredcare.org</span><span><i class="dot-orange"></i>www.kindredcare.org</span></div></footer>
</section>

<!-- Page 9: questions and signatures -->
<section class="page col-left row-5">
  <div class="brand"><span class="brand-dot"></span><span class="brand-name">KINDRED CARE</span></div>
  <div class="form-tab"><div class="tab">ONBOARDING FORM</div><div class="tab-note">(Please Read and Sign)</div></div>
  <div class="content">
    <div class="panel" style="padding-top:12px;padding-bottom:22px">
      <span class="pill pill-blue">QUESTION &amp; COMMENTS</span>
      <div class="grid g1" style="margin-bottom:18px"><div class="field"><label>Question/Comment 1</label><div class="box mid"></div></div></div>
      <div class="grid g1" style="margin-bottom:18px"><div class="field"><label>Question/Comment 2</label><div class="box mid"></div></div></div>
      <div class="grid g1" style="margin-bottom:0"><div class="field"><label>Question/Comment 3</label><div class="box mid"></div></div></div>
    </div>
    <span class="pill pill-pink" style="margin-top:28px;margin-bottom:24px">CONSENT &amp; SIGNATURE</span>
    <div class="sign-grid">
      <div class="field"><label>Patient Assistance Fund</label><div class="box"></div></div>
      <div class="field"><label>Assignment of Benefits</label><div class="box"></div></div>
      <div class="field" style="margin-top:14px"><label>Consent Forms</label><div class="box"></div></div>
      <div class="field" style="margin-top:14px"><label>HIPAA Data Use Agreement</label><div class="box"></div></div>
    </div>
  </div>
  <footer class="footer"><div class="footer-bar"></div><div class="footer-items"><span><i class="dot-blue"></i>+1 (555) 010 2480</span><span><i class="dot-purple"></i>info@kindredcare.org</span><span><i class="dot-orange"></i>www.kindredcare.org</span></div></footer>
</section>

</body>
</html>
```